Dr K.L. Fenwick, Consultant General Surgeon

Modern minimalistic look [shades of blue should be included]
I would like an interactive website which gives information about
1. Home page: office location
Medical Partners
📞(876) 555-0192-7
📱(876) 555-0147
📍42 Marigold Crescent, Kingston 10

VelaMedix
1-876-555-0163 / 1-876-555-0178 / 1-876-555-0129
📍37 North Cedar Grove RD, Kingston, Jamaica (Upstairs Brisa Linwood)
Info@velamedix.example

Beacon Care Medical Suites
📞(876) 555-0184
📱(876) 555-0136
📍Shop 22-23, Palm Crest Shopping Mall, Portmore

Corwell Medical Centre
📞 (876) 555-0151
📍 9 Pellowin Street , May Pen
The office logos will be attached
Booking details on this page or 2nd page with procedures

2. My surgical services . - I will attach a business card with the information for this section - do not upload the actual business card on the site

3. Allow the booking of appointments at any of the offices
4. A section where short explainer videos will be uploaded (this section is titled "Surgery in 3D"- I will upload an example below
5. A section- which shows videos of procedures. This section is titled "Surgical procedures" - I will upload one below
these videos will similar the same as the ones on my Instagram account
Link: https://www.instagram.com/dr_klfenwick?igsh=QmVyZXhhbXBsZQ&utm_source=qr

6. Gallery- section with pictures from interviews/ presentations/conferences etc

Each section should be on a different page.
The clearly defined sections can be represented from a HOME PAGE or drop-down menu
SIMILAR websites:
Modern professional design style (fonts and layout)- https://brightscalpelstudio.example
others -- this best captures the style I'm looking for. I prefer if the page is not crowded
https://velamedix.example
layered effect -- https://quillbankclinic.example/general-surgeon/
https://drpetrahalvik.example

I have updated the brief

Target Market(s)

Patients who require general surgical care

Coding

Coded - Design and coding required

Number of Pages Required

5+ page

Requirements
Must have
• Each section should be on a different page.

```html
<!DOCTYPE html>
<html lang="en">
<head>
<meta charset="utf-8">
<title>Dr K.L. Fenwick – Consultant General Surgeon</title>
<link rel="stylesheet" href="https://fonts.googleapis.com/css2?family=Poppins:wght@400;500;600;700&display=swap">
<style>
:root{
  --navy:#0b2a5a;
  --navy-deep:#082148;
  --blue:#0aa2f0;
  --blue-text:#1b8fd6;
  --ink:#0c1a2e;
  --muted:#4a5568;
  --bg-light:#f5f7fb;
  --bg-grey:#e9edf3;
  --white:#ffffff;
}
*{box-sizing:border-box;margin:0;padding:0}
html,body{width:1200px;height:4611px;overflow:hidden}
body{font-family:"Poppins",sans-serif;color:var(--ink);background:var(--white);position:relative}
.section{position:absolute;left:0;width:1200px}
.eyebrow{font-size:13px;color:var(--blue-text);text-transform:uppercase;letter-spacing:.2px}
.h2{font-size:34px;font-weight:600;color:var(--ink);line-height:1.5}
.btn{display:inline-flex;align-items:center;justify-content:center;background:var(--blue);color:#fff;border-radius:30px;font-weight:600;text-decoration:none}
.link-under{position:absolute;color:var(--blue-text);font-size:17px;border-bottom:1px solid var(--blue-text);padding-bottom:4px}
.ph{position:absolute;border-radius:4px}
.play{position:absolute;width:56px;height:56px;border-radius:50%;background:#fff;left:50%;top:50%;transform:translate(-50%,-50%)}
.play::after{content:"";position:absolute;left:21px;top:15px;border-left:20px solid #000;border-top:13px solid transparent;border-bottom:13px solid transparent}

/* nav + hero */
.hero{top:0;height:675px;background:linear-gradient(90deg,#0a2a5c 0%,#0f3a78 45%,#1f5b99 100%)}
.hero-photo{position:absolute;left:560px;top:0;width:640px;height:675px;background:linear-gradient(90deg,rgba(15,58,120,0) 0%,#3d6fa3 35%,#2a4a70 70%,#1b2f4d 100%)}
.nav{position:absolute;top:0;left:0;width:1200px;height:93px;background:var(--navy-deep)}
.brand{position:absolute;display:flex;align-items:center;gap:12px}
.brand .mark{width:40px;height:40px;border-radius:50%;border:2px solid #fff}
.brand .name{color:#fff;font-weight:700;font-size:18px;line-height:1.1}
.brand .sub{color:#fff;font-size:6.5px;letter-spacing:1.2px;font-weight:600}
.menu{position:absolute;right:93px;top:38px;display:flex;gap:20px;color:#fff;font-size:13px}
.hero h1{position:absolute;left:93px;top:222px;color:#fff;font-size:45px;font-weight:600;line-height:1.32}
.hero p{position:absolute;left:93px;top:373px;color:#e3ecf7;font-size:16px;line-height:1.85;width:560px}
.hero .btn{position:absolute;left:93px;top:480px;width:451px;height:55px;font-size:16px}

/* locations */
.locations{top:675px;height:579px;background:var(--bg-light)}
.locations .eyebrow{position:absolute;top:94px;width:100%;text-align:center}
.locations .h2{position:absolute;top:118px;width:100%;text-align:center}
.card{position:absolute;top:210px;width:240px;height:297px;background:#fff;border:1px solid #e3e8ef;box-shadow:0 2px 8px rgba(0,0,0,.06);border-radius:4px}
.card .logo{position:absolute;top:22px;left:0;width:100%;height:60px;display:flex;align-items:center;justify-content:center;font-size:15px;font-weight:600;color:var(--navy)}
.card h3{position:absolute;left:15px;top:99px;font-size:14px;font-weight:600}
.card ul{position:absolute;left:15px;top:136px;width:215px;list-style:none;font-size:11px;line-height:1.65;color:#333}
.card li{display:flex;gap:5px}
.card li svg{flex:none;margin-top:3px}
.card .btn{position:absolute;left:15px;bottom:15px;width:190px;height:36px;font-size:12px}

/* services */
.services{top:1254px;height:818px;background:var(--bg-grey)}
.services .eyebrow{position:absolute;left:93px;top:61px}
.services .h2{position:absolute;left:93px;top:80px}
.services .link-under{left:922px;top:91px}
.tile{position:absolute;width:281px;height:281px;background:var(--navy);border-radius:4px}
.tile .ph{left:18px;top:18px;width:307px;height:207px;border-radius:2px}
.tile span{position:absolute;right:-40px;top:226px;width:320px;text-align:right;color:#fff;font-size:18px;padding-right:60px}

/* 3d */
.guide{top:2072px;height:539px;background:var(--bg-light)}
.guide .eyebrow{position:absolute;left:93px;top:59px}
.guide .h2{position:absolute;left:93px;top:86px;line-height:1.55}
.guide .btn{position:absolute;left:93px;top:239px;width:317px;height:55px;font-size:15px}
.frame3d{position:absolute;left:480px;top:61px;width:627px;height:419px;background:#000;border-radius:12px;padding:18px}
.frame3d .ph{position:relative;display:block;width:100%;height:100%;border-radius:10px;background:linear-gradient(135deg,#ffffff 0%,#e8f3f6 45%,#9cc7d3 100%)}

/* procedures */
.procedures{top:2611px;height:537px;background:var(--bg-grey)}
.vid{position:absolute;width:278px;height:199px;border-radius:4px}
.procedures .eyebrow{position:absolute;left:729px;top:60px}
.procedures .h2{position:absolute;left:729px;top:84px;line-height:1.55}
.procedures .btn{position:absolute;left:729px;top:238px;width:313px;height:57px;font-size:15px}

/* gallery */
.gallery{top:3148px;height:724px;background:var(--bg-light)}
.gallery .eyebrow{position:absolute;left:93px;top:60px}
.gallery .h2{position:absolute;left:93px;top:83px}
.gallery .link-under{left:991px;top:92px}
.shot{position:absolute;width:326px;height:235px;border-radius:2px}

/* about */
.about{top:3872px;height:435px;background:var(--navy)}
.about .eyebrow{position:absolute;left:93px;top:57px;color:var(--blue)}
.about h2{position:absolute;left:93px;top:80px;color:#fff;font-size:34px;font-weight:600;line-height:1.35}
.about p{position:absolute;left:93px;top:201px;width:500px;color:#dbe5f2;font-size:15.5px;line-height:1.4}
.about .btn{position:absolute;left:93px;top:327px;width:202px;height:56px;font-size:15px;font-weight:500}
.about-photo{position:absolute;left:760px;top:0;width:330px;height:435px;background:linear-gradient(180deg,#0b2a5a 0%,#15355f 40%,#1c2a3f 100%)}

/* footer */
.footer{top:4307px;height:304px;background:var(--navy-deep);border-top:1px solid #1d3b6c}
.footer .brand{left:93px;top:95px}
.footer .brand .mark{width:58px;height:58px}
.footer .brand .name{font-size:26px}
.footer .brand .sub{font-size:9px}
.ig{position:absolute;left:93px;top:172px;width:34px;height:34px;border:2px solid #b7c4d6;border-radius:9px}
.copy{position:absolute;left:93px;top:230px;color:#b7c4d6;font-size:11px}
.fcol{position:absolute;top:63px;color:#c8d3e3;font-size:13px;line-height:27px;list-style:none}
.fcol h4{color:#fff;font-size:17px;font-weight:600;margin-bottom:4px}
</style>
</head>
<body>

<header class="section hero">
  <div class="hero-photo" role="img" aria-label="Portrait of the surgeon in a dark suit and blue tie, with a masked surgeon in scrubs faintly in the background"></div>
  <nav class="nav">
    <div class="brand" style="left:97px;top:26px">
      <span class="mark"></span>
      <div><div class="name">DR. K.L. FENWICK</div><div class="sub">CONSULTANT GENERAL SURGEON</div></div>
    </div>
    <div class="menu">
      <span>Home</span><span>About</span><span>Locations ⌄</span><span>Surgical Services ⌄</span><span>Surgical Procedures</span><span>Gallery</span><span>Contact Us</span>
    </div>
  </nav>
  <h1>Exceptional Surgical Care.<br>Compassionate Expertise</h1>
  <p>Explore our locations, book an appointment, or learn more about our surgical services.</p>
  <a class="btn">Schedule an Appointment Today →</a>
</header>

<section class="section locations">
  <div class="eyebrow">Conveniently located offices for comprehensive surgical care across <b>Jamaica.</b></div>
  <h2 class="h2">Explore Our Locations</h2>

  <div class="card" style="left:93px">
    <div class="logo">Medical Partners</div>
    <h3>Medical Partners</h3>
    <ul>
      <li><svg width="9" height="9" viewBox="0 0 10 10"><path d="M2 0l2 2-1 2 3 3 2-1 2 2-2 2C4 10 0 6 0 2z" fill="#333"/></svg>(876) 555-0192-7</li>
      <li><svg width="9" height="9" viewBox="0 0 10 10"><rect x="2" y="0" width="6" height="10" rx="1" fill="#333"/></svg>(876) 555-0147</li>
      <li><svg width="9" height="9" viewBox="0 0 10 10"><path d="M5 0a3.5 3.5 0 0 1 3.5 3.5C8.5 6 5 10 5 10S1.5 6 1.5 3.5A3.5 3.5 0 0 1 5 0z" fill="#e0312b"/></svg>42 Marigold Crescent, Kingston 10</li>
    </ul>
    <a class="btn">Book an Appointment</a>
  </div>

  <div class="card" style="left:351px">
    <div class="logo">VelaMedix</div>
    <h3>VelaMedix</h3>
    <ul style="top:128px;font-size:10.5px;line-height:1.7">
      <li><svg width="9" height="9" viewBox="0 0 10 10"><path d="M2 0l2 2-1 2 3 3 2-1 2 2-2 2C4 10 0 6 0 2z" fill="#333"/></svg>1-876-555-0163/ 1-876-555-0178/</li>
      <li><svg width="9" height="9" viewBox="0 0 10 10"><path d="M2 0l2 2-1 2 3 3 2-1 2 2-2 2C4 10 0 6 0 2z" fill="#333"/></svg>1-876-555-0129</li>
      <li><svg width="9" height="9" viewBox="0 0 10 10"><path d="M5 0a3.5 3.5 0 0 1 3.5 3.5C8.5 6 5 10 5 10S1.5 6 1.5 3.5A3.5 3.5 0 0 1 5 0z" fill="#e0312b"/></svg>37 North Cedar Grove RD, Kingston, Jamaica (Upstairs Brisa Linwood)</li>
      <li>Info@velamedix.example</li>
    </ul>
    <a class="btn">Book an Appointment</a>
  </div>

  <div class="card" style="left:609px">
    <div class="logo">Beacon Care</div>
    <h3>Beacon Care Medical Suites</h3>
    <ul>
      <li><svg width="9" height="9" viewBox="0 0 10 10"><path d="M2 0l2 2-1 2 3 3 2-1 2 2-2 2C4 10 0 6 0 2z" fill="#333"/></svg>(876) 555-0184</li>
      <li><svg width="9" height="9" viewBox="0 0 10 10"><rect x="2" y="0" width="6" height="10" rx="1" fill="#333"/></svg>(876) 555-0136</li>
      <li><svg width="9" height="9" viewBox="0 0 10 10"><path d="M5 0a3.5 3.5 0 0 1 3.5 3.5C8.5 6 5 10 5 10S1.5 6 1.5 3.5A3.5 3.5 0 0 1 5 0z" fill="#e0312b"/></svg>Shop 22-23, Palm Crest Shopping Mall, Portmore</li>
    </ul>
    <a class="btn">Book an Appointment</a>
  </div>

  <div class="card" style="left:867px">
    <div class="logo">Corwell</div>
    <h3>Corwell Medical Centre</h3>
    <ul>
      <li><svg width="9" height="9" viewBox="0 0 10 10"><path d="M2 0l2 2-1 2 3 3 2-1 2 2-2 2C4 10 0 6 0 2z" fill="#333"/></svg>(876) 555-0151</li>
      <li><svg width="9" height="9" viewBox="0 0 10 10"><path d="M5 0a3.5 3.5 0 0 1 3.5 3.5C8.5 6 5 10 5 10S1.5 6 1.5 3.5A3.5 3.5 0 0 1 5 0z" fill="#e0312b"/></svg>9 Pellowin Street , May Pen</li>
    </ul>
    <a class="btn" style="bottom:18px">Book an Appointment</a>
  </div>
</section>

<section class="section services">
  <div class="eyebrow">Advanced Surgical Solutions</div>
  <h2 class="h2">My Surgical Services</h2>
  <span class="link-under">Browse All Services →</span>

  <div class="tile" style="left:93px;top:177px"><div class="ph" role="img" aria-label="Man in grey shirt holding his lower back in pain" style="background:linear-gradient(135deg,#f2f2f2,#9a9c9e 60%,#6f8a80)"></div><span>Hernia Repair</span></div>
  <div class="tile" style="left:437px;top:177px"><div class="ph" role="img" aria-label="Woman in beige top holding a breast cancer ribbon" style="background:linear-gradient(135deg,#8a5a3e,#c59f85 50%,#b78d73)"></div><span>Breast Cancer Surgery</span></div>
  <div class="tile" style="left:781px;top:177px"><div class="ph" role="img" aria-label="Nurse in teal scrubs checking a patient's abdomen" style="background:linear-gradient(135deg,#3a9a8e,#cfd6dc 55%,#a48aa6)"></div><span>Gallbladder Surgery</span></div>

  <div class="tile" style="left:93px;top:476px"><div class="ph" role="img" aria-label="Man in white t-shirt holding his stomach" style="background:linear-gradient(135deg,#8f9294,#b4b6b7 50%,#7b7e80)"></div><span>Appendix</span></div>
  <div class="tile" style="left:437px;top:476px"><div class="ph" role="img" aria-label="Person in crop top showing a small lump on the abdomen" style="background:linear-gradient(135deg,#3a3530,#b49a85 50%,#7a5c48)"></div><span>Lump Excision</span></div>
  <div class="tile" style="left:781px;top:476px"><div class="ph" role="img" aria-label="Shirtless man clutching his abdomen" style="background:linear-gradient(135deg,#2a211c,#6e4c3a 50%,#cfcfcf)"></div><span>Colorectal</span></div>
</section>

<section class="section guide">
  <div class="eyebrow">Understanding Surgery in 3D</div>
  <h2 class="h2">Guide to Our<br>Surgical Processes</h2>
  <a class="btn">Schedule an Appointment Today →</a>
  <div class="frame3d">
    <div class="ph" role="img" aria-label="Surgery in 3D explainer video cover in teal"><span class="play" style="background:#000;left:44%;top:47%"></span></div>
  </div>
</section>

<section class="section procedures">
  <div class="vid" role="img" aria-label="Surgeons in blue gowns operating" style="left:93px;top:61px;background:linear-gradient(135deg,#2f6fc0,#6fa2de 60%,#9fc2ea)"><span class="play"></span></div>
  <div class="vid" role="img" aria-label="Operating theatre team at work" style="left:390px;top:61px;background:linear-gradient(135deg,#3b4a55,#5c86b8 50%,#8fb5de)"><span class="play"></span></div>
  <div class="vid" role="img" aria-label="Surgeon in blue gown at the table" style="left:93px;top:280px;background:linear-gradient(135deg,#3d7ac8,#76a6db 50%,#4e7f9a)"><span class="play"></span></div>
  <div class="vid" role="img" aria-label="Surgeon wearing a headlamp and mask" style="left:390px;top:280px;background:linear-gradient(135deg,#e8f0f8,#7ea8da 50%,#2f6bbf)"><span class="play"></span></div>
  <div class="eyebrow">Surgical Procedures in Action</div>
  <h2 class="h2">Explore Surgical<br>Procedures</h2>
  <a class="btn">Schedule an Appointment Today →</a>
</section>

<section class="section gallery">
  <div class="eyebrow">Proud to present my achievements</div>
  <h2 class="h2">Explore Gallery</h2>
  <span class="link-under">Visit Gallery →</span>
  <div class="shot" role="img" aria-label="Three surgeons in suits at a conference" style="left:93px;top:178px;background:linear-gradient(135deg,#7d8fa8,#2b3550 55%,#c5b59a)"></div>
  <div class="shot" role="img" aria-label="Surgeon standing before an annual meeting banner" style="left:437px;top:178px;background:linear-gradient(135deg,#d9cfa8,#e9e5d8 50%,#8fa8b8)"></div>
  <div class="shot" role="img" aria-label="Television segment about a thyroid condition" style="left:781px;top:178px;background:linear-gradient(135deg,#c0392b,#1d3b6a 55%,#7fa8cf)"></div>
  <div class="shot" role="img" aria-label="Two doctors posing at an event" style="left:93px;top:432px;background:linear-gradient(135deg,#ffffff,#c5cbd3 50%,#2f3c5c)"></div>
  <div class="shot" role="img" aria-label="Surgeon in white coat in a clinic" style="left:437px;top:432px;background:linear-gradient(135deg,#e6eaee,#aab4be 50%,#3b4350)"></div>
  <div class="shot" role="img" aria-label="Surgeon teaching a group of students" style="left:781px;top:432px;background:linear-gradient(135deg,#d8d4ce,#a88a78 50%,#c0464a)"></div>
</section>

<section class="section about">
  <div class="eyebrow">Meet your surgeon</div>
  <h2>Hi, I’m Dr. K.L. Fenwick<br>MBBS, DM</h2>
  <p>With a passion for precision and a dedication to patient well-being, I strive to provide life-changing surgical care. Every patient’s journey is unique, and I am here to guide you with expertise and empathy.</p>
  <a class="btn">Learn More →</a>
  <div class="about-photo" role="img" aria-label="Portrait of the surgeon in a dark suit and blue tie"></div>
</section>

<footer class="section footer">
  <div class="brand">
    <span class="mark"></span>
    <div><div class="name">DR. K.L. FENWICK</div><div class="sub">CONSULTANT GENERAL SURGEON</div></div>
  </div>
  <span class="ig"></span>
  <div class="copy">© 2024 Dr. K.L. Fenwick</div>
  <ul class="fcol" style="left:607px">
    <h4>Quick Links</h4>
    <li>Home</li><li>About</li><li>Surgical Services</li><li>Surgical Procedures</li><li>Gallery</li><li>Contact</li>
  </ul>
  <ul class="fcol" style="left:930px">
    <h4>Offices/Locations</h4>
    <li>Medical Partners</li><li>VelaMedix</li><li>Beacon Care Medical Suites</li><li>Corwell Medical Centre</li>
  </ul>
</footer>

</body>
</html>
```